Digital Marketing Website Redesign, modern, fresh, dynamic

Hi there, we would like to freshen up our website and create a new dynamic look. We are a digital marketing agency who specialise in digital transformation in the form of creating websites for appointment bookings. Our clients are service businesses such as hairdressers, dentists and doctors who's patients need to book appointments with them.

Our company name is Plombek with the point being we can help increase your revenue curve by increasing your appointment bookings.

Our services include building the website, creating campaigns to drive traffic, increasing conversions and monitoring and reporting.

We are playing with a tagline of 'Step into your Digital Transformation' as we have a 5 step journey that customers can take with us getting them from zero to full appointment bookings.

Our current website is www.plomnbek-site.example

You can see a draft design that I mocked up on Canva here https://www.drawpadhub.example/design/QXT82LmnB7K/PoWz41kdRtGyvb_sxE_JNq/edit?utm_content=QXT82LmnB7K&utm_campaign=designshare&utm_medium=link2&utm_source=sharebutton

Also attached some other homepage ideas. In regard to photos we are open to ideas.

Please let if you need any more information to provide us with an initial design. Thanks million and I look forward to receiving fantastic designs :)

Marissa Tobler
Plombek

Target Market(s)

Appointment based businesses such as hairdressers, dentists, doctors

Industry/Entity Type

Marketing and Digital

Coding

Coded - Design and coding required

Number of Pages Required

1 page

Colors
0094D4
00A9DD
6FCCEA
C7EBF8
E9F6FB

Requirements
Must have
• Appointment booking CTA
Nice to have
• A website we like https://www.morwenhalbrook.example

```html
<!DOCTYPE html>
<html lang="en">
<head>
<meta charset="utf-8">
<title>Plombek – Step Into Your Digital Transformation</title>
<link href="https://fonts.googleapis.com/css2?family=Abril+Fatface&family=Roboto:wght@300;400;500;700&display=swap" rel="stylesheet">
<style>
:root{
  --blue:#0094D4;
  --blue-2:#00A9DD;
  --blue-3:#6FCCEA;
  --blue-4:#C7EBF8;
  --blue-5:#E9F6FB;
  --navy:#1e63a8;
  --ink:#111;
  --text:#444;
  --muted:#9a9a9a;
  --white:#fff;
  --panel:#f1f1f1;
  --display:"Abril Fatface", Georgia, serif;
  --sans:"Roboto", Arial, sans-serif;
}
*{box-sizing:border-box;margin:0;padding:0}
html,body{width:1200px;height:3948px;overflow:hidden}
body{position:relative;font-family:var(--sans);color:var(--text);background:var(--white)}
a{color:inherit;text-decoration:none}

/* nav */
.nav{position:absolute;left:0;top:0;width:1200px;height:62px;border-bottom:1px solid #e5e5e5;background:#fff}
.brand{position:absolute;left:100px;top:18px;font-family:var(--sans);font-weight:700;font-size:22px;color:var(--navy);display:flex;align-items:center;gap:6px}
.brand .dot{width:8px;height:8px;border-radius:50%;background:var(--blue)}
.nav-links{position:absolute;left:405px;top:23px;display:flex;gap:24px;font-size:11px;color:#444}
.nav-links .active{color:#111;font-weight:500;text-decoration:underline}
.nav-cta{position:absolute;left:1008px;top:12px;width:100px;height:37px;border:1.5px solid #222;font-size:11px;font-weight:700;color:#111;display:flex;align-items:center;justify-content:center;box-shadow:2px 2px 0 #ddd}

/* hero */
.hero{position:absolute;left:0;top:62px;width:1200px;height:604px;background:radial-gradient(ellipse at 50% 45%,#bfefff 0%,#4fb6e8 12%,#135b9a 38%,#0a2748 70%,#061628 100%)}
.hero h1{position:absolute;left:0;width:1200px;top:88px;text-align:center;font-family:var(--display);font-weight:400;font-size:74px;line-height:90px;color:#fff;letter-spacing:1px}
.hero p{position:absolute;left:340px;width:520px;top:412px;text-align:center;font-size:14px;line-height:18px;color:#fff}
.hero .btn{position:absolute;left:528px;top:495px;width:147px;height:34px;border:1.5px solid #fff;color:#fff;font-size:10px;font-weight:700;display:flex;align-items:center;justify-content:center}

/* stats */
.stat{position:absolute;top:770px;width:200px;text-align:center}
.stat svg{display:block;margin:0 auto}
.stat .num{font-family:var(--display);font-size:40px;color:#666;line-height:44px;margin-top:2px}
.stat .lbl{font-size:10px;color:#aaa}

/* pricing */
.plan{position:absolute;top:982px;width:270px;height:363px;border:1.5px solid var(--blue-3);border-radius:0 0 14px 14px;background:#fff;padding:18px 0 0 30px}
.plan h3{font-family:var(--display);font-weight:400;font-size:21px;color:var(--navy);line-height:22px}
.plan .sub{font-size:10px;color:var(--blue-3)}
.plan .price{font-family:var(--display);font-size:52px;color:var(--navy);text-align:center;margin:12px 30px 0 0;line-height:56px}
.plan .per{font-size:10px;color:var(--blue);text-align:center;margin-right:30px}
.plan .per.right{text-align:right;margin-right:55px}
.plan ul{list-style:none;margin-top:16px}
.plan li{font-size:13.5px;line-height:20px;color:#444;display:flex;align-items:center;gap:4px}
.plan li.plain{padding-left:16px}
.tick{width:12px;height:12px;flex:none}

/* case studies */
.cases{position:absolute;left:0;top:1426px;width:1200px;height:510px;background:var(--blue)}
.tabs{position:absolute;left:667px;top:81px;display:flex;gap:12px}
.tab{height:22px;padding:0 12px;border:1.5px solid #fff;color:#fff;font-size:10px;font-weight:700;display:flex;align-items:center}
.tab.on{background:#fff;color:#111}
.cases h2{position:absolute;left:165px;top:110px;font-family:var(--display);font-weight:400;font-size:66px;line-height:72px;color:#fff}
.cases p{position:absolute;left:163px;top:266px;width:300px;font-size:11px;line-height:20px;color:#fff}
.cases .btn{position:absolute;left:163px;top:350px;width:130px;height:35px;border:1.5px solid #fff;color:#fff;font-size:10px;font-weight:700;display:flex;align-items:center;justify-content:center}
.case-img{position:absolute;top:147px;height:281px}

/* experience */
.exp-img1{position:absolute;left:81px;top:2016px;width:367px;height:356px;background:linear-gradient(135deg,#d9d6d0,#b89a6a 55%,#8d8d8d)}
.exp-img2{position:absolute;left:393px;top:2058px;width:204px;height:207px;border-radius:0 0 14px 0;background:linear-gradient(160deg,#eceae6,#c9b6a6 60%,#9b5a4a)}
.exp h2{position:absolute;left:642px;top:2045px;font-family:var(--display);font-weight:400;font-size:64px;line-height:72px;color:#111}
.exp p{position:absolute;left:641px;top:2210px;width:480px;font-size:11px;line-height:20px;color:#555}
.exp p b{color:var(--blue);font-weight:500}
.exp .btn{position:absolute;left:641px;top:2296px;width:130px;height:36px;border:1.5px solid var(--blue);color:#111;font-size:10px;font-weight:700;display:flex;align-items:center;justify-content:center;box-shadow:2px 2px 0 var(--blue-4)}

/* testimonial */
.testi{position:absolute;left:0;top:2502px;width:1200px;height:498px;background:linear-gradient(90deg,#3d3a36 0%,#5a5651 40%,#4a4845 70%,#3a3a3b 100%)}
.testi h2{position:absolute;left:163px;top:70px;font-family:var(--display);font-weight:400;font-size:62px;line-height:72px;color:#fff}
.testi .quote{position:absolute;left:460px;top:238px;font-size:14px;line-height:25px;color:#fff;font-weight:500}
.testi .who{position:absolute;left:460px;top:336px;display:flex;gap:14px}
.testi .who i{display:block;width:38px;height:2px;background:#fff;margin-top:10px}
.testi .who b{display:block;font-family:var(--display);font-weight:400;font-size:19px;color:#fff;line-height:20px}
.testi .who span{font-size:13px;color:#ddd}
.dots{position:absolute;left:460px;top:398px;display:flex;gap:7px;align-items:center}
.dots i{width:4px;height:4px;border-radius:50%;background:#fff}
.dots i.on{width:7px;height:7px}

/* partners */
.partners{position:absolute;left:153px;top:3092px;width:875px;height:174px;background:var(--panel)}
.partners .head{position:absolute;left:45px;right:45px;top:43px;height:20px;border-top:1px solid #999;margin-top:10px}
.partners .head span{position:absolute;left:50%;transform:translate(-50%,-11px);background:var(--panel);padding:0 8px;font-family:Georgia,serif;font-weight:700;font-size:13px;color:#222;white-space:nowrap}
.marks{position:absolute;left:45px;right:45px;top:90px;display:flex;justify-content:space-between;align-items:center}
.mark{font-size:22px;font-weight:500;color:#555;display:flex;align-items:center;gap:6px}
.mark i{width:18px;height:18px;border-radius:50%;background:#888;display:block}

/* newsletter */
.hello h2{position:absolute;left:0;width:1200px;top:3322px;text-align:center;font-family:var(--display);font-weight:400;font-size:64px;color:#111}
.hello .s1{position:absolute;left:0;width:1200px;top:3426px;text-align:center;font-size:21px;color:#777;font-weight:300}
.hello .s2{position:absolute;left:0;width:1200px;top:3458px;text-align:center;font-size:20px;color:#222}
.form{position:absolute;left:363px;top:3532px;width:429px;height:48px;border:1px solid #333;border-right:none}
.form span{position:absolute;left:25px;top:17px;font-size:9px;color:#777}
.form b{position:absolute;right:0;top:6px;width:131px;height:36px;background:#000;border:1.5px solid var(--blue);color:#fff;font-size:10px;display:flex;align-items:center;justify-content:center}

/* footer */
.footer{position:absolute;left:0;top:3668px;width:1200px;height:280px;background:#000;color:#fff}
.footer .brand{left:163px;top:64px;color:var(--blue-2)}
.footer .about{position:absolute;left:163px;top:120px;width:205px;font-size:9px;line-height:17px;color:#ddd}
.socials{position:absolute;left:163px;top:187px;display:flex;gap:16px}
.socials i{width:24px;height:24px;background:#fff;display:block}
.fcol{position:absolute;top:64px}
.fcol h4{font-size:14px;font-weight:500;margin-bottom:26px}
.fcol a{display:block;font-size:9px;color:#ddd;line-height:24px}
.fcol .row{display:flex;gap:8px;align-items:center;font-size:9px;color:#ddd;line-height:27px}
.copy{position:absolute;left:0;width:1200px;top:258px;text-align:center;font-size:9px;color:#ddd}
</style>
</head>
<body>

<header class="nav">
  <div class="brand"><span class="dot"></span>Plombek</div>
  <nav class="nav-links">
    <a class="active">Home</a><a>About</a><a>Services</a><a>Case Studies</a><a>Apps</a><a>Pricing</a>
  </nav>
  <a class="nav-cta">GET START</a>
</header>

<section class="hero" role="img" aria-label="Person walking through a glowing blue digital tunnel">
  <h1>Step Into<br>Your Digital<br>Transformation</h1>
  <p>Digital Transformation Is A Journey. At Plombek We Divide The Journey Into Five Key Steps That Take Your Business From Comprehensive Market Research To Full Appointment Bookings. Ready To Go On That Journey?</p>
  <a class="btn">LET'S GET STARTED</a>
</section>

<section class="stats">
  <div class="stat" style="left:145px">
    <svg width="52" height="50" viewBox="0 0 52 50" fill="none" stroke="#666" stroke-width="3"><rect x="4" y="8" width="44" height="38" rx="2"/><line x1="4" y1="18" x2="48" y2="18"/><line x1="15" y1="2" x2="15" y2="12"/><line x1="37" y1="2" x2="37" y2="12"/><polyline points="17,31 23,37 35,25"/></svg>
    <div class="num">762</div><div class="lbl">Appointments Booked</div>
  </div>
  <div class="stat" style="left:370px">
    <svg width="52" height="50" viewBox="0 0 52 50" fill="none" stroke="#666" stroke-width="3"><path d="M6 18h10l20-12v36L16 30H6z"/><path d="M12 30l4 14h6l-3-14"/><path d="M42 18q5 6 0 12"/></svg>
    <div class="num">31</div><div class="lbl">Marketing Companies</div>
  </div>
  <div class="stat" style="left:602px">
    <svg width="52" height="50" viewBox="0 0 52 50" fill="#666"><rect x="4" y="30" width="5" height="16"/><rect x="13" y="20" width="5" height="26"/><rect x="22" y="4" width="5" height="42"/><rect x="31" y="14" width="5" height="32"/><rect x="40" y="26" width="5" height="20"/></svg>
    <div class="num">25%</div><div class="lbl">Website Traffic Increase</div>
  </div>
  <div class="stat" style="left:815px">
    <svg width="52" height="72" viewBox="0 0 52 72" fill="none" stroke="#666" stroke-width="3"><path d="M26 2a18 18 0 0 0-11 32v8h22v-8A18 18 0 0 0 26 2z"/><path d="M28 12l-8 12h10l-6 10"/><path d="M17 62c-10 0-10-12 0-12s12 12 18 12 10-12 0-12-8 12-18 12z"/></svg>
    <div class="lbl" style="margin-top:8px">Creative Ideas</div>
  </div>
</section>

<svg width="0" height="0" style="position:absolute"><defs><symbol id="tick" viewBox="0 0 12 12"><circle cx="6" cy="6" r="6" fill="#0094D4"/><polyline points="3,6.2 5.2,8.3 9,4" fill="none" stroke="#fff" stroke-width="1.6"/></symbol></defs></svg>

<section class="pricing">
  <article class="plan" style="left:146px">
    <h3>Starter Plan</h3><div class="sub">Build A Beautiful Website</div>
    <div class="price">€6,999</div><div class="per right">Initial Set Up Fee</div>
    <ul>
      <li><svg class="tick"><use href="#tick"/></svg>Homepage</li>
      <li><svg class="tick"><use href="#tick"/></svg>Landing pages</li>
      <li><svg class="tick"><use href="#tick"/></svg>Usability - platform adaptability</li>
      <li><svg class="tick"><use href="#tick"/></svg>Performance</li>
      <li><svg class="tick"><use href="#tick"/></svg>SEO</li>
      <li><svg class="tick"><use href="#tick"/></svg>Payment gateway</li>
      <li><svg class="tick"><use href="#tick"/></svg>Online booking app</li>
    </ul>
  </article>
  <article class="plan" style="left:465px">
    <h3>Premium Plan</h3><div class="sub">Online Marketing</div>
    <div class="price">€499</div><div class="per">For A Month</div>
    <ul>
      <li><svg class="tick"><use href="#tick"/></svg>Market research</li>
      <li><svg class="tick"><use href="#tick"/></svg>Marketing Campaigns</li>
      <li><svg class="tick"><use href="#tick"/></svg>Conversion Rate Performance</li>
      <li><svg class="tick"><use href="#tick"/></svg>Scalability</li>
      <li><svg class="tick"><use href="#tick"/></svg>Social Compelling content</li>
      <li><svg class="tick"><use href="#tick"/></svg>Get online bookings</li>
      <li><svg class="tick"><use href="#tick"/></svg>GDPR compliance</li>
      <li class="plain">Chat bot / AI integration/ Coach</li>
    </ul>
  </article>
  <article class="plan" style="left:783px;top:980px">
    <h3>Ultimate Plan</h3><div class="sub">Monitor And Maintain</div>
    <div class="price">€899</div><div class="per">For A Month</div>
    <ul style="margin-top:20px">
      <li><svg class="tick"><use href="#tick"/></svg>Indepth reporting</li>
      <li><svg class="tick"><use href="#tick"/></svg>Customer review</li>
      <li><svg class="tick"><use href="#tick"/></svg>Industry updates</li>
      <li><svg class="tick"><use href="#tick"/></svg>Buying cycle alignment</li>
      <li><svg class="tick"><use href="#tick"/></svg>Digital tools and technologies</li>
    </ul>
  </article>
</section>

<section class="cases">
  <div class="tabs"><span class="tab on">ALL</span><span class="tab">MARKETING</span><span class="tab">BRANDING</span><span class="tab">SEO</span><span class="tab">WEB</span></div>
  <h2>Our Case<br>Studies</h2>
  <p>Ad Nec Unum Copiosae. Sea Ex Everti Labores, Ad Option Iuvaret Qui. Id Quo Esse Nusquam.</p>
  <a class="btn">VIEW ALL CASES</a>
  <div class="case-img" role="img" aria-label="Woman emerging from a phone surrounded by social media icons" style="left:510px;width:304px;background:linear-gradient(135deg,#6b4a3a,#c98a5a 45%,#e3b070 60%,#5a3a30)"></div>
  <div class="case-img" role="img" aria-label="Large smartphone beside a man holding a coat on blue background" style="left:834px;width:303px;background:linear-gradient(135deg,#4d9ec6,#3a8ab6 50%,#6a8a78)"></div>
  <div class="case-img" role="img" aria-label="Next case study preview" style="left:1155px;width:45px;background:linear-gradient(135deg,#dfe6ea,#9aa8b0)"></div>
</section>

<section class="exp">
  <div class="exp-img1" role="img" aria-label="Woman holding a tablet with floating notification icons"></div>
  <div class="exp-img2" role="img" aria-label="Excited man pointing to the side"></div>
  <h2>Digital<br>Experience</h2>
  <p>Step Into The Future Of Digital Excellence With <b>Plombek</b>. Our Blend Of Sleek Design And Advanced Tech Ensures A Smooth And Captivating User Experience. Explore Innovation At Your Fingertips – Welcome To A Redefined Digital Space!</p>
  <a class="btn">DISCOVER MORE</a>
</section>

<section class="testi" role="img" aria-label="Group of smiling business people in an office">
  <h2>What People<br>Say</h2>
  <div class="quote">From 55 New Patients Per Month!<br>Since Plombek Optimised Our Marketing Campaigns We've<br>Had 55-75 New Patients Per Month.</div>
  <div class="who"><i></i><div><b>Dr. Halvar Quint</b><span>Owner, Brightmolar</span></div></div>
  <div class="dots"><i></i><i></i><i class="on"></i><i></i></div>
</section>

<section class="partners">
  <div class="head"><span>OVER 1K+ BUSINESSES GROWING WITH MARKET</span></div>
  <div class="marks">
    <span class="mark" style="font-size:16px"><i></i>Zelvorin</span>
    <span class="mark">Pextrawl</span>
    <span class="mark">Quomblix</span>
    <span class="mark" style="font-size:19px">varnesko</span>
    <span class="mark" style="font-size:26px">druxelle</span>
  </div>
</section>

<section class="hello">
  <h2>Say Hello To Market!</h2>
  <div class="s1">Sing Up For Newsletter And Receive</div>
  <div class="s2">40% Discount On First Project</div>
  <div class="form"><span>Email Address</span><b>SUBSCRIBE NOW</b></div>
</section>

<footer class="footer">
  <div class="brand"><span class="dot"></span>Plombek</div>
  <p class="about">It is a long established fact that a reader will be distracted by the readable content of a page when looking at its layout</p>
  <div class="socials"><i></i><i></i><i></i><i></i></div>
  <div class="fcol" style="left:493px">
    <h4>Our services</h4>
    <a>SEO Marketing</a><a>SEO Services</a><a>Pay Per Click</a><a>Social Media</a><a>SEO Audit</a>
  </div>
  <div class="fcol" style="left:703px">
    <h4>Quick link</h4>
    <a>Home</a><a>About Us</a><a>Main Services</a><a>Pricing</a><a>Our Cases</a>
  </div>
  <div class="fcol" style="left:895px">
    <h4>Contact us</h4>
    <div class="row"><svg width="9" height="11" viewBox="0 0 9 11"><path d="M4.5 0a4 4 0 0 0-4 4c0 3 4 7 4 7s4-4 4-7a4 4 0 0 0-4-4z" fill="#fff"/><circle cx="4.5" cy="4" r="1.5" fill="#000"/></svg>14 Larkfield Row, Dunmore</div>
    <div class="row"><svg width="10" height="8" viewBox="0 0 10 8" fill="none" stroke="#fff"><rect x=".5" y=".5" width="9" height="7"/><polyline points=".5,.5 5,4.5 9.5,.5"/></svg>hello@plombek-mail.example</div>
    <div class="row"><svg width="10" height="8" viewBox="0 0 10 8" fill="none" stroke="#fff"><rect x=".5" y=".5" width="9" height="7"/><polyline points=".5,.5 5,4.5 9.5,.5"/></svg>+1 (555) 014-2270</div>
  </div>
  <div class="copy">Copyright © 2024 <b>Market</b>. All Rights Reserved.</div>
</footer>

</body>
</html>
```